www.brevatin.com Sales/Order Page ReDesign

We need a new and amazing design for our sales/order page to attract more costumers and new houses for our portal.

Here is the existing page with the current design: https://www.brevatin.com/sales

We are proud owners of www.sommarhytta.no and www.brevatin.com and we want more holiday home owners to join our page so that we can rent out their holiday homes and increase the number of houses on our portal.

To get more homeowners we need a sales page that can sell our products the best way possible. Therefore we want you too blow us away with a fresh, modern, easy understandable and stylish new sales/order page.

The only restrictions we give when it comes to design is that it needs to fit the existing design of our portals, the top and footer are set. Beside that we are open for everything as long as it at once give the customers impression that this is a good, professional page were they just have to put out their houses.

When it comes to content I have added two documents who include the content to put in here and some guidelines on how to organize the page. Please be creative and add necessary graphics, symbols, background pictures and what ever necessary to make this page look professional and appealing to new costumers.

Looking forward to what suggestions we are given.

We just want to inform that we have updated our brief with a much more concrete description of what content to add on the sale page, and who to structure the content on the page. Hope this helps to make suggestions easier. Looking forward to receive some good contributions.

We would just like to make sure that everyone have understood that we are not asking for a new design suggestion to our portal in general. We are only asking for a redesign of our sales/order page you find here www.brevatin.com/sales. We have to day received some designs for our front page and the design it self was good, but that's not what we are asking for this time and don't want you to use time of something we don't need at the moment. We are looking forward too se some good suggestions.

Reason: Hello. Thanks for all the great contributions we have been given so fare. We haven't been able to respond to all design and are therefore extending the deadline so that we are able to respond to the designs we have been giver and to gov time to make final changes.

Reason: We are extending the deadline to give designers time to give new suggestion based on our latest feedback today.

Reason: Extended so we can receive last design changes.

Target Market(s)

This is a presentation page where we present our product agains new home owner who we what to choose listing there property on or site.

Industry/Entity Type

Sales

Requirements
Must have
• A modern design who calms the costumer down and help them in deciding to chose us, and for them to choose us they need to trust and believe in us. Therefore your main task is to create a page that effectively informs about our product, gets the visitors attentions and make them trust us.
Nice to have
• Examples of good competitors and good order pages we like:

http://www.cabinquest.example/info/lyp?icid=IL___O_Text___top_nav_link
https://www.nestlodge.example/rooms/new
https://www.pearvix.example/phone/compare/
http://www.guestnook.example/host
Should not have
• - Bad design :-). With bad design we mean design that looks like it's made in 2 seconds by a little child.

```html
<!DOCTYPE html>
<html lang="en">
<head>
<meta charset="utf-8">
<title>Brevatin – List Your Property</title>
<link href="https://fonts.googleapis.com/css2?family=Roboto:wght@300;400;500;700&family=Shadows+Into+Light&display=swap" rel="stylesheet">
<style>
:root{
  --page-bg:#f4f4f4;
  --brand-blue:#2a9fd8;
  --bar-blue:#1e90d6;
  --ink:#333333;
  --ink-soft:#6b6b6b;
  --muted:#9a9a9a;
  --card:#ffffff;
  --cream:#fff9d9;
  --green:#8cc63f;
  --green-dark:#6fa82a;
  --tab-shadow:#444a52;
  --stamp-red:#c8202a;
  --ic-blue:#4a9fd8;
  --ic-yellow:#f4b72c;
  --ic-pink:#c45a80;
  --ic-red:#d9383a;
  --ic-cyan:#36a3da;
  --ic-green:#3fbf80;
  --ic-purple:#a56cc8;
  --ic-olive:#a9963e;
  --ic-brown:#8b5a3c;
  --ic-gold:#f0cd1c;
  --ic-lime:#6cc05a;
}
*{margin:0;padding:0;box-sizing:border-box}
html,body{width:720px;height:1200px;overflow:hidden}
body{background:var(--page-bg);font-family:'Roboto',Arial,sans-serif;color:var(--ink);position:relative}
.abs{position:absolute}

.top-bar{left:0;top:0;width:720px;height:34px;background:var(--bar-blue)}
.brand-tab{left:78px;top:0;width:204px;height:104px}
.brand-name{left:118px;top:20px;font-size:30px;font-weight:500;color:var(--brand-blue);letter-spacing:.5px}
.brand-mark{left:94px;top:26px;width:20px;height:20px;background:var(--brand-blue);border-radius:50%}
.brand-sub{left:166px;top:55px;font-size:10px;color:var(--brand-blue);letter-spacing:.5px}
.flag{top:10px;width:16px;height:12px}
.flag-no{left:410px;background:#c8202a}
.flag-gb{left:432px;background:#1f3f8a}
.sign-in{left:464px;top:5px;width:96px;height:24px;background:var(--green);border:1px solid var(--green-dark);border-radius:2px;color:#fff;font-size:10px;font-weight:500;display:flex;align-items:center;padding-left:28px}
.list-link{left:566px;top:11px;font-size:10px;font-weight:700;color:#fff}

.hero-title{left:0;width:720px;top:114px;text-align:center;font-size:20px;font-weight:400;color:var(--brand-blue)}
.hero-sub{left:0;width:720px;top:142px;text-align:center;font-size:11px;color:var(--ink-soft)}
.hand-note{left:80px;top:172px;width:120px;text-align:center;font-family:'Shadows Into Light',cursive;font-size:17px;line-height:17px;color:var(--muted)}
.hand-arrow{left:120px;top:206px;width:100px;height:40px}
.promo-card{left:214px;top:168px;width:430px;height:86px;background:linear-gradient(#fff 60%,var(--cream));box-shadow:0 1px 3px rgba(0,0,0,.25)}
.promo-photo{left:3px;top:3px;width:139px;height:80px;background:linear-gradient(#5fb4e8 0%,#8fd0ee 40%,#2cb5b0 70%,#3e7d3a 100%)}
.promo-head{left:160px;top:20px;font-size:15px;color:var(--ink)}
.promo-text{left:160px;top:42px;width:240px;font-size:10px;line-height:13px;color:var(--ink-soft)}

.section-title{left:0;width:720px;text-align:center;font-size:18px;font-weight:300;color:var(--brand-blue)}
.divider-glow{left:160px;width:400px;height:14px;background:radial-gradient(ellipse at top,rgba(0,0,0,.08),transparent 70%)}

.service{width:270px}
.service.wide{width:480px}
.service-icon{position:absolute;left:0;top:0;width:46px;height:46px;display:flex;align-items:center;justify-content:center}
.service-icon svg{width:28px;height:28px}
.service-body{margin-left:54px}
.service-title{font-size:13px;font-weight:400;color:var(--ink);margin-top:-2px}
.service-text{font-size:8.4px;line-height:11px;color:var(--ink-soft);margin-top:3px}

.list-question{left:0;width:720px;top:957px;text-align:center;font-size:15px;color:var(--ink)}
.option{background:linear-gradient(#fff 60%,var(--cream));box-shadow:0 1px 3px rgba(0,0,0,.22)}
.option-row{position:absolute;display:flex;align-items:flex-start;gap:8px;font-size:11px;line-height:13px;color:var(--ink-soft)}
.opt-ic{width:14px;height:14px;border-radius:50%;background:#8a8a8a;flex:none;margin-top:1px}
.option-sep{position:absolute;height:1px;background:#e6e6e6}

.rule{left:78px;width:570px;height:1px;background:#d8d8d8}
.discount-badge{left:94px;top:1106px;width:76px;height:70px;border-radius:50%;border:4px solid var(--stamp-red);opacity:.85}
.discount-title{left:190px;top:1120px;font-size:16px;font-weight:300;color:var(--muted)}
.discount-sub{left:190px;top:1142px;font-size:11px;color:var(--ink)}
.discount-arrow{left:300px;top:1128px;width:140px;height:36px}
.qty-label{left:444px;top:1121px;font-size:9px;color:var(--ink)}
.qty-input{left:444px;top:1138px;width:91px;height:18px;background:#fff;border:1px solid #d4d4d4;font-size:9px;color:var(--muted);padding:4px 6px}
</style>
</head>
<body>

<header>
  <div class="abs top-bar"></div>
  <svg class="abs brand-tab" viewBox="0 0 204 104" aria-hidden="true">
    <polygon points="0,0 204,0 204,90 102,62 0,90" fill="#fff"/>
    <polygon points="0,90 102,62 204,90 204,104 102,76 0,104" fill="var(--tab-shadow)"/>
  </svg>
  <span class="abs brand-mark"></span>
  <div class="abs brand-name">Brevatin</div>
  <div class="abs brand-sub">HOLIDAY RENTAL</div>
  <span class="abs flag flag-no" role="img" aria-label="Norwegian language"></span>
  <span class="abs flag flag-gb" role="img" aria-label="English language"></span>
  <div class="abs sign-in">Sign in</div>
  <div class="abs list-link">List your property</div>
</header>

<main>
  <h1 class="abs hero-title">List Your Property Today!</h1>
  <p class="abs hero-sub">Brevatin helps you make money on your property, starting now...</p>
  <div class="abs hand-note">On Brevatin<br>you can rent out</div>
  <svg class="abs hand-arrow" viewBox="0 0 100 40" aria-hidden="true">
    <path d="M4 4 C10 30 50 36 92 30" fill="none" stroke="#a0a0a0" stroke-width="1.5"/>
    <path d="M84 24 L93 30 L84 35" fill="none" stroke="#a0a0a0" stroke-width="1.5"/>
  </svg>
  <div class="abs promo-card">
    <div class="abs promo-photo" role="img" aria-label="Photo of a thatched beach house by turquoise water"></div>
    <div class="abs promo-head">And make a profit on it. You ask how?</div>
    <div class="abs promo-text">Keep reading and we will let you know how <b><i>easy</i></b> and <b><i>hassle free</i></b> it is!</div>
  </div>

  <h2 class="abs section-title" style="top:304px">All our announcements have the following services included:</h2>
  <div class="abs divider-glow" style="top:334px"></div>

  <div class="abs service wide" style="left:82px;top:362px">
    <div class="service-icon" style="background:var(--ic-blue)"><svg viewBox="0 0 28 28"><circle cx="14" cy="8" r="5" fill="#fff"/><path d="M5 26 C5 17 23 17 23 26Z" fill="#fff"/></svg></div>
    <div class="service-body"><div class="service-title">Help from professionals</div>
    <div class="service-text">Let professionals who know the travel industries handle all yours booking requests. Great result with less work, our professional team will answer all you inquiries, while you spend time with friends, family and enjoy your own holiday.</div></div>
  </div>

  <div class="abs service" style="left:82px;top:434px">
    <div class="service-icon" style="background:var(--ic-yellow)"><svg viewBox="0 0 28 28"><rect x="6" y="10" width="16" height="15" fill="#fff"/><path d="M10 10 V7 a4 4 0 0 1 8 0 V10" fill="none" stroke="#fff" stroke-width="2"/></svg></div>
    <div class="service-body"><div class="service-title">Access Scandinavians</div>
    <div class="service-text">Our roots are from Norway, and we have expertise with the Scandinavian market and can help you get tenants from these very travel friendly demographics.</div></div>
  </div>
  <div class="abs service" style="left:367px;top:434px">
    <div class="service-icon" style="background:var(--ic-pink)"><svg viewBox="0 0 28 28"><path d="M4 14 L14 5 L24 14 V25 H4Z" fill="#fff"/><rect x="11" y="17" width="6" height="8" fill="var(--ic-pink)"/></svg></div>
    <div class="service-body"><div class="service-title">Broad exposure</div>
    <div class="service-text">We have been in the market for several years and are promoting your property through the necessary and right channels.</div></div>
  </div>

  <div class="abs service" style="left:82px;top:506px">
    <div class="service-icon" style="background:var(--ic-red)"><svg viewBox="0 0 28 28"><circle cx="14" cy="14" r="11" fill="none" stroke="#fff" stroke-width="2.5"/><line x1="6" y1="22" x2="22" y2="6" stroke="#fff" stroke-width="2.5"/></svg></div>
    <div class="service-body"><div class="service-title">No Traveler fees</div>
    <div class="service-text">Unlike many other vacation rental booking sites, travelers can book vacation rentals without paying any fees to us, maybe one of the reason we have so many returning costumers.</div></div>
  </div>
  <div class="abs service" style="left:367px;top:506px">
    <div class="service-icon" style="background:var(--ic-cyan)"><svg viewBox="0 0 28 28"><circle cx="14" cy="14" r="11" fill="none" stroke="#fff" stroke-width="2.5"/><rect x="3" y="11" width="22" height="6" fill="#fff"/></svg></div>
    <div class="service-body"><div class="service-title">Trust &amp; Safety</div>
    <div class="service-text">You are still in control of your property. We have the tools to help you accept a booking only if you're 100% comfortable.</div></div>
  </div>

  <div class="abs service" style="left:82px;top:577px">
    <div class="service-icon" style="background:var(--ic-green)"><svg viewBox="0 0 28 28"><rect x="5" y="5" width="18" height="18" fill="none" stroke="#fff" stroke-width="2"/><circle cx="14" cy="14" r="5" fill="#fff"/></svg></div>
    <div class="service-body"><div class="service-title">Payments by Brevatin</div>
    <div class="service-text">Guests are always carful when it comes to payment. Everybody can feel safe through secure payment with Brevatin. We are responsible for you getting paid.</div></div>
  </div>
  <div class="abs service" style="left:367px;top:577px">
    <div class="service-icon" style="background:var(--ic-purple)"><svg viewBox="0 0 28 28"><rect x="5" y="5" width="16" height="16" fill="none" stroke="#fff" stroke-width="2" stroke-dasharray="3 2"/><path d="M13 13 L24 17 L19 19 L17 24Z" fill="#fff"/></svg></div>
    <div class="service-body"><div class="service-title">Online Booking</div>
    <div class="service-text">We simplify the booking process by allowing tenants to send online reservations request, which gives you a 24-hour period to accept or decline their reservation.</div></div>
  </div>

  <div class="abs service" style="left:82px;top:648px">
    <div class="service-icon" style="background:var(--ic-olive)"><svg viewBox="0 0 28 28"><line x1="6" y1="6" x2="22" y2="22" stroke="#fff" stroke-width="3.5"/><line x1="22" y1="6" x2="6" y2="22" stroke="#fff" stroke-width="3.5"/></svg></div>
    <div class="service-body"><div class="service-title">Easy-to-Use Tools</div>
    <div class="service-text">Get access too a very well developed reservation and management tool that helps you keep track of bookings.</div></div>
  </div>
  <div class="abs service" style="left:367px;top:648px">
    <div class="service-icon" style="background:var(--ic-blue)"><svg viewBox="0 0 28 28"><rect x="6" y="4" width="16" height="20" fill="none" stroke="#fff" stroke-width="2"/><path d="M11 11 a3 3 0 1 1 3 3 v3" fill="none" stroke="#fff" stroke-width="2"/><circle cx="14" cy="20" r="1.2" fill="#fff"/></svg></div>
    <div class="service-body"><div class="service-title">Unlimited inquiries</div>
    <div class="service-text">When you are renting out your property you need inquiries, therefore we have no fees on inquiries for your property.</div></div>
  </div>

  <div class="abs service" style="left:82px;top:720px">
    <div class="service-icon" style="background:var(--ic-brown)"><svg viewBox="0 0 28 28"><rect x="5" y="6" width="18" height="18" fill="#fff"/><rect x="5" y="6" width="18" height="4" fill="#d9c9bf"/></svg></div>
    <div class="service-body"><div class="service-title">Online calendar</div>
    <div class="service-text">Tenants like to know when your property is available straight away, and we let them know that. At the same time you can easily manage your availability.</div></div>
  </div>
  <div class="abs service" style="left:367px;top:720px">
    <div class="service-icon" style="background:var(--ic-gold)"><svg viewBox="0 0 28 28"><rect x="4" y="7" width="20" height="15" fill="#fff"/><circle cx="14" cy="14.5" r="4" fill="var(--ic-gold)"/></svg></div>
    <div class="service-body"><div class="service-title">Unlimited photos</div>
    <div class="service-text">A picture says more then 1000 words, therefore we inspire you too upload as many pictures as possible.</div></div>
  </div>

  <div class="abs service" style="left:82px;top:790px">
    <div class="service-icon" style="background:var(--ic-lime)"><svg viewBox="0 0 28 28"><path d="M14 24 C8 16 7 13 7 10 a7 7 0 0 1 14 0 c0 3 -1 6 -7 14Z" fill="none" stroke="#fff" stroke-width="2"/><circle cx="14" cy="10" r="2.5" fill="#fff"/></svg></div>
    <div class="service-body"><div class="service-title">Map and location</div>
    <div class="service-text">Tenants are always wondering where your property is located. Show them through our map and let them know where nearby attractions are.</div></div>
  </div>

  <h2 class="abs section-title" style="top:900px">Getting impressed now, wait to you see our low prices...</h2>
  <div class="abs divider-glow" style="top:930px"></div>

  <h3 class="abs list-question" style="font-weight:400">How do you want to list your property?</h3>

  <div class="abs option" style="left:77px;top:991px;width:350px;height:85px">
    <div class="option-row" style="left:12px;top:11px"><span class="opt-ic"></span><span>Save time while we create income on your property</span></div>
    <div class="option-sep" style="left:10px;right:10px;top:32px"></div>
    <div class="option-row" style="left:12px;top:37px;width:330px"><span class="opt-ic"></span><span>Let our professional team handle your inquiries and bookings, and just sit and wait for the costumer to arrive at your property knowing you will get paid.</span></div>
  </div>
  <div class="abs option" style="left:439px;top:991px;width:208px;height:85px">
    <div class="option-row" style="left:12px;top:11px"><span class="opt-ic"></span><span>Do it yourself</span></div>
    <div class="option-sep" style="left:10px;right:10px;top:32px"></div>
    <div class="option-row" style="left:12px;top:37px;width:180px"><span class="opt-ic"></span><span>Handle inquiries and bookings yourself, with help with our advance tools</span></div>
  </div>

  <div class="abs rule" style="top:1100px"></div>
  <div class="abs discount-badge" role="img" aria-label="Discount stamp"></div>
  <div class="abs discount-title">Get discounts</div>
  <div class="abs discount-sub">if you have more than one property</div>
  <svg class="abs discount-arrow" viewBox="0 0 140 36" aria-hidden="true">
    <path d="M80 30 C110 30 125 22 134 10" fill="none" stroke="#a0a0a0" stroke-width="1.5"/>
    <path d="M126 10 L135 8 L134 17" fill="none" stroke="#a0a0a0" stroke-width="1.5"/>
  </svg>
  <div class="abs qty-label">Type in the number of properties:</div>
  <div class="abs qty-input">6</div>
  <div class="abs rule" style="top:1182px"></div>
</main>

</body>
</html>
```